Nanotechnology meets nature cosmetic company needs label design. Name of the company is QuillaBloom

We are a cosmetic brand that combines nanotechnology with nature in the form of hemp extracts and essential oils, creating products that provide pain relief as well as stress reduction and relaxation. We have three different products and need three separate labels. We have a logo and would like to incorporate that into the label design. The colors are teal, black and gray. We would like to convey a message of combining nature with cutting edge cosmetic technology.
1. Topical pain lotion
2. Bath soak
3. Massage lotion
The logo is attached and I would just like the logo used and not the text below. The colors of the logo should be teal cross and "V" inside the gray lines that make up the circle with black color inside the circle. If this can't be done, I can send another logo.

```html
<!DOCTYPE html>
<html lang="en">
<head>
<meta charset="utf-8">
<title>QuillaBloom — Topical Pain Lotion Label</title>
<link rel="stylesheet" href="https://fonts.googleapis.com/css2?family=Saira+Condensed:wght@600;800&family=Open+Sans:wght@400&display=swap">
<style>
  :root {
    --page: #e9e9e7;
    --label-black: #121414;
    --label-deep: #0f2624;
    --teal: #2a9d8f;
    --teal-bright: #34b3a2;
    --leaf-glow: #7fd36b;
    --silver: #b9bcbd;
    --panel-white: #f4f4f2;
    --body-text: #2b2b2b;
  }
  * { box-sizing: border-box; margin: 0; padding: 0; }
  html, body { width: 1200px; height: 1200px; overflow: hidden; background: var(--page); }
  .canvas { position: relative; width: 1200px; height: 1200px; }

  .label {
    position: absolute; left: 40px; top: 250px; width: 1120px; height: 700px;
    background:
      repeating-linear-gradient(180deg, transparent 0 22px, rgba(42,157,143,0.16) 22px 24px),
      linear-gradient(180deg, var(--label-black), var(--label-deep) 55%, var(--label-black));
    overflow: hidden;
  }

  .info-panel {
    position: absolute; left: 0; top: 40px; width: 120px; height: 600px;
    background: var(--panel-white); border-radius: 0 22px 22px 0;
    padding: 24px 12px 24px 10px;
    font-family: "Open Sans", sans-serif; font-size: 14px; line-height: 1.45;
    color: var(--body-text); text-align: right;
  }

  .brand {
    position: absolute; left: 200px; top: 120px;
    display: flex; align-items: center; gap: 16px;
  }
  .brand-dot {
    width: 46px; height: 46px; border-radius: 50%;
    background: var(--teal);
  }
  .brand-name {
    font-family: "Saira Condensed", sans-serif; font-weight: 800;
    font-size: 64px; color: var(--teal); letter-spacing: 1px;
  }

  .leaf {
    position: absolute; width: 90px; height: 90px; border-radius: 50%;
    background: radial-gradient(circle, rgba(127,211,107,0.75), rgba(127,211,107,0.08) 70%);
  }
  .leaf--left { left: 165px; top: 375px; }
  .leaf--right { left: 575px; top: 395px; }

  .product-title {
    position: absolute; left: 250px; top: 350px;
    font-family: "Saira Condensed", sans-serif; font-weight: 800;
    color: var(--teal-bright); text-transform: uppercase; line-height: 0.95;
  }
  .product-title .line-one { display: block; font-size: 118px; padding-left: 12px; }
  .product-title .line-two { display: block; font-size: 126px; margin-left: -50px; }

  .net-weight {
    position: absolute; left: 430px; top: 600px;
    font-family: "Saira Condensed", sans-serif; font-weight: 600;
    font-size: 40px; color: var(--teal);
  }

  .body-figure {
    position: absolute; left: 640px; top: 60px; width: 420px; height: 600px;
    border-radius: 50%;
    background: radial-gradient(ellipse at center, rgba(150,185,185,0.55), rgba(42,157,143,0.18) 55%, transparent 72%);
  }
</style>
</head>
<body>
<main class="canvas">
  <section class="label">
    <aside class="info-panel">
      Soothing blend of hemp extract and essential oils with nano delivery. Massage gently into skin over sore areas. For external use only. Avoid eyes. Store cool and dry.
    </aside>

    <div class="brand">
      <span class="brand-dot"></span>
      <span class="brand-name">QuillaBloom</span>
    </div>

    <div class="leaf leaf--left" role="img" aria-label="Glowing hemp leaf illustration"></div>
    <div class="leaf leaf--right" role="img" aria-label="Glowing hemp leaf illustration"></div>

    <h1 class="product-title">
      <span class="line-one">Topical</span>
      <span class="line-two">Pain Lotion</span>
    </h1>

    <p class="net-weight">16oz</p>

    <div class="body-figure" role="img" aria-label="Illustration of a human silhouette with glowing red pain points inside technical rings"></div>
  </section>
</main>
</body>
</html>
```